Web design for Money Service Business (uncoded)

We need a very basic website with 5-6 pages. Home page, Services, Transfer(How to use our service), About us, Contact us, FAQ
Our company name is Meridale Exchange. We are a company that deals with currency exchange and international money transfer. We do cash exchange and international money transfers to bank accounts all over the world. We offer highly competitive exchange rates so usually attract customers who transfer money over $10,000. Our niche is with larger sums of money, the design needs to be professional and communicate trust, security and stability.

```html
<!DOCTYPE html>
<html lang="en">
<head>
<meta charset="utf-8">
<title>Meridale Exchange — Home</title>
<link href="https://fonts.googleapis.com/css2?family=Open+Sans:ital,wght@0,300;0,400;0,600;0,700;1,400;1,700&display=swap" rel="stylesheet">
<style>
:root{
  --brand-blue:#1e5a8a;
  --ink:#555a5e;
  --ink-soft:#7b7f82;
  --panel:#e6e7e8;
  --white:#ffffff;
  --footer:#141414;
  --footer-text:#8c8c8c;
  --button-grey:#a7a9ab;
}
*{box-sizing:border-box;margin:0;padding:0}
html,body{width:803px;height:1200px;overflow:hidden;background:var(--white)}
body{position:relative;font-family:"Open Sans",Arial,sans-serif;color:var(--ink)}

.site-header{position:absolute;left:0;top:0;width:803px;height:107px;background:var(--white)}
.brand{position:absolute;left:36px;top:34px;display:flex;align-items:center;gap:8px}
.brand-mark{width:26px;height:26px;border-radius:50%;background:var(--brand-blue)}
.brand-text{display:flex;flex-direction:column}
.brand-name{font-size:25px;font-weight:700;color:var(--brand-blue);line-height:26px;letter-spacing:.2px}
.brand-tagline{font-size:9.4px;color:var(--brand-blue);letter-spacing:2.1px;line-height:13px}
.main-nav{position:absolute;left:326px;top:55px;display:flex;align-items:center;font-size:14.5px;color:var(--ink)}
.main-nav a{color:inherit;text-decoration:none}
.main-nav .current{background:var(--brand-blue);color:var(--white);height:28px;line-height:28px;padding:0 12px;margin-right:11px}
.main-nav .sep{margin:0 10px}

.hero{position:absolute;left:0;top:107px;width:803px;height:328px;background:var(--brand-blue)}
.hero-photo{position:absolute;left:39px;top:0;width:725px;height:328px;
  background:linear-gradient(180deg,#e9ecef 0%,#d9dcdf 45%,#3a3e48 75%,#2b2e36 100%)}
.hero-arrow{position:absolute;top:150px;width:30px;height:50px}
.hero-arrow.prev{left:3px}
.hero-arrow.next{left:770px}

.intro{position:absolute;left:35px;top:435px;width:733px;height:183px;background:var(--panel)}
.intro h1{position:absolute;left:98px;top:24px;font-size:16.5px;font-weight:700;color:var(--ink)}
.intro .lead{position:absolute;left:120px;top:45px;width:470px;font-size:10.2px;font-style:italic;line-height:13px}
.intro .body{position:absolute;left:101px;top:84px;width:560px;font-size:12.3px;line-height:14.5px}

.cta-band{position:absolute;left:0;top:618px;width:803px;height:91px;background:var(--brand-blue)}
.cta-band h2{position:absolute;left:100px;top:30px;font-size:23px;font-weight:700;font-style:italic;color:var(--white)}
.cta-button{position:absolute;left:517px;top:30px;width:118px;height:33px;background:linear-gradient(180deg,#c3c5c7,var(--button-grey));
  border:2px solid #ededed;color:#33363a;font-size:13.5px;text-align:center;line-height:29px}

.news{position:absolute;left:35px;top:709px;width:733px;height:401px;background:var(--panel)}
.news h2{position:absolute;left:40px;top:44px;font-size:16.5px;font-weight:700;color:var(--ink)}
.news-item{position:absolute;top:79px;width:196px}
.news-image{width:193px;height:139px}
.news-item h3{margin-top:10px;font-size:14px;font-weight:400;font-style:italic;color:var(--ink)}
.news-item p{margin-top:3px;font-size:10.4px;line-height:12.9px;text-align:justify;color:var(--ink-soft);font-weight:300}

.site-footer{position:absolute;left:0;top:1110px;width:803px;height:90px;background:var(--footer)}
.footer-nav{position:absolute;left:53px;top:23px;font-size:10.8px;color:var(--footer-text)}
.footer-nav .current{color:var(--white)}
.footer-nav .sep{margin:0 6px}
.copyright{position:absolute;left:53px;top:53px;font-size:10.8px;color:var(--footer-text)}
.social{position:absolute;left:528px;top:46px;display:flex;gap:14px;align-items:center}
.back-to-top{position:absolute;left:691px;top:53px;width:28px;height:40px;background:#5f6163;border-radius:14px 14px 0 0}
</style>
</head>
<body>

<header class="site-header">
  <div class="brand">
    <span class="brand-mark"></span>
    <div class="brand-text">
      <span class="brand-name">Meridale Exchange</span>
      <span class="brand-tagline">INTERNATIONAL MONEY TRANSFER</span>
    </div>
  </div>
  <nav class="main-nav">
    <a class="current" href="#">Home</a>
    <a href="#">Services</a><span class="sep">|</span>
    <a href="#">Transfer</a><span class="sep">|</span>
    <a href="#">About Us</a><span class="sep">|</span>
    <a href="#">Contact Us</a><span class="sep">|</span>
    <a href="#">FAQ</a>
  </nav>
</header>

<section class="hero">
  <div class="hero-photo" role="img" aria-label="Photo of a smiling business team gathered around a meeting table with a laptop"></div>
  <svg class="hero-arrow prev" viewBox="0 0 30 50"><polyline points="24,5 5,25 24,45" fill="none" stroke="#fff" stroke-width="3"/></svg>
  <svg class="hero-arrow next" viewBox="0 0 30 50"><polyline points="6,5 25,25 6,45" fill="none" stroke="#fff" stroke-width="3"/></svg>
</section>

<section class="intro">
  <h1>Lorem ipsum dolor sit amet, consectetur adipisicing elit</h1>
  <p class="lead">ed do eiusmod tempor incididunt ut labore et dolore magna aliqua. Ut enim ad minim veniam, quis nostrud exercitation ullamco laboris nisi</p>
  <p class="body">Sed ut perspiciatis, unde omnis iste natus error sit voluptatem accusantium doloremque laudantium, totam rem aperiam eaque ipsa, quae ab illo inventore veritatis et quasi architecto beatae vitae dicta sunt, explicabo. Nemo enim ipsam voluptatem, quia voluptas sit, aspernatur aut odit aut fugit, sed quia consequuntur magni dolores eos, qui ratione voluptatem sequi nesciunt, neque porro quisquam est</p>
</section>

<section class="cta-band">
  <h2>Need more information about us ?</h2>
  <div class="cta-button">Contact Us</div>
</section>

<section class="news">
  <h2>Recent News</h2>
  <article class="news-item" style="left:40px">
    <div class="news-image" role="img" aria-label="Photo of a finger touching a tablet screen" style="background:linear-gradient(135deg,#2e6f80,#8fb7c2 50%,#d8c3b0)"></div>
    <h3>Fast Conection</h3>
    <p>Lorem ipsum dolor sit amet, consectetur adipisicing elit, sed do eiusmod tempor incididunt ut labore et dolore magna aliqua. Ut enim ad minim veniam, quis nostrud exercitation ullamco laboris nisi ut aliquip ex ea commodo consequat. Duis aute irure dolor in reprehenderit in voluptate velit esse cillum dolore eu fugiat nulla pariatur. Excepteur sint</p>
  </article>
  <article class="news-item" style="left:265px">
    <div class="news-image" role="img" aria-label="Photo of an open hand with floating screens of business images" style="background:linear-gradient(135deg,#3d5a85,#e3e3e3 50%,#2a2a2a)"></div>
    <h3>All Busines in Your Hand</h3>
    <p>Lorem ipsum dolor sit amet, consectetur adipisicing elit, sed do eiusmod tempor incididunt ut labore et dolore magna aliqua. Ut enim ad minim veniam, quis nostrud exercitation ullamco laboris nisi ut aliquip ex ea commodo consequat. Duis aute irure dolor in reprehenderit in voluptate velit esse cillum dolore eu fugiat nulla pariatur. Excepteur sint</p>
  </article>
  <article class="news-item" style="left:490px">
    <div class="news-image" role="img" aria-label="Photo of a hand sketching gears on a dark board" style="background:linear-gradient(135deg,#2c2f36,#4a4e58 60%,#23252a)"></div>
    <h3>Easy Maintenance</h3>
    <p>Lorem ipsum dolor sit amet, consectetur adipisicing elit, sed do eiusmod tempor incididunt ut labore et dolore magna aliqua. Ut enim ad minim veniam, quis nostrud exercitation ullamco laboris nisi ut aliquip ex ea commodo consequat. Duis aute irure dolor in reprehenderit in voluptate velit esse cillum dolore eu fugiat nulla pariatur. Excepteur sint</p>
  </article>
</section>

<footer class="site-footer">
  <nav class="footer-nav">
    <span class="current">Home</span><span class="sep">|</span>Services<span class="sep">|</span>Transfer<span class="sep">|</span>About Us<span class="sep">|</span>Contact US<span class="sep">|</span>FAQ
  </nav>
  <p class="copyright">Copyright © 2013 All Right Reserved by www.harlowe-studio.com</p>
  <div class="social">
    <svg width="20" height="14" viewBox="0 0 20 14" aria-label="Email"><rect x="1" y="1" width="18" height="12" rx="1.5" fill="none" stroke="#8c8c8c" stroke-width="2"/><polyline points="2,2 10,8 18,2" fill="none" stroke="#8c8c8c" stroke-width="2"/></svg>
    <svg width="18" height="18" viewBox="0 0 18 18" aria-label="Social link"><circle cx="9" cy="9" r="8" fill="#8c8c8c"/></svg>
    <svg width="18" height="18" viewBox="0 0 18 18" aria-label="Social link"><circle cx="9" cy="9" r="8" fill="#8c8c8c"/></svg>
    <svg width="16" height="16" viewBox="0 0 16 16" aria-label="Feed"><rect x="0" y="0" width="16" height="16" rx="3" fill="#8c8c8c"/></svg>
  </div>
  <div class="back-to-top">
    <svg width="28" height="20" viewBox="0 0 28 20"><polyline points="9,13 14,8 19,13" fill="none" stroke="#fff" stroke-width="1.6"/></svg>
  </div>
</footer>

</body>
</html>
```